REALTOR/REALESTATE INVESTOR CARD

I AM MY LOCAL CITIES FLIP THIS HOUSE KING...I CHANGE NEIGHBORHOODS ONE HOUSE AT A TIME. I BUY OLD HOUSES FOR CASH TOTALLY RENOVATE THEM TO LIKE NEW, THEN RE SELL THEM...
I HAVE BEEN USING PLATINUM & BURGANDY AS MY MAIN COLOR..
I WANT SOMETHING FUN AND MODERN TO APPEAL TO ALL BUYERS AND SELLERS. AND TO REFLECT I AM AT THE TOP OF MY GAME...A WOW...THIS IS A GREAT CARD.......WOW.......I AM A REALTOR....I FLIP HOUSES.....MAYBE SHOW AND OLD HOUSE AND THEN A SPARKLING NEW HOUSE..... MY COMPANY NAME IS HOMESTEAD CAPITAL PARTNERS THE ADDRESS IS P.O.BOX 86 MARSH HOLLOW, S.C. 29401

Target Market(s)

I SELL HOUSES THAT HAVE BEEN RENOVATED TO ALMOST BRAND NEW CONDITION.......I ALSO BUY HOUSES/MOBILES FOR ALL CASH FAST CLOSINGS..
I BUY MARSH HOLLOW HOUSES ALL CASH FAST CLOSE.....I BUY MOBILE HOMES ANY CONDITION, ANY PRICE.....Buyers & sellers of houses.....

Industry/Entity Type

Investment

Font styles to use
Sans Serif

Requirements
Must have
• I BUY MARSH HOLLOW HOMES FOR CASH, QUICK CLOSINGS......
RENEWING MARSH HOLLOW, ONE HOME AT A TIME...
RAY T. BELLAMY CIAS
REALTOR/CERTIFIED INVESTOR AGENT
HOMESTEAD CAPITAL PARTNERS,LLC.
P.O. BOX 86
MARSH HOLLOW, S.C. 29401
843-555-0172
RAYBELLAMYHOUSES@QUILLMAIL.EXAMPLE
Nice to have
• MARSH HOLLOW'S RE-HAB KING....
A actual picture of MAYBE A HOME BEING RENOVATED
TO ONE LOOKING AWESOME.....artwork
Should not have
• a picture of and old ugly home the a sparkling brand new one that is what I di I renovate homes.......

```html
<!DOCTYPE html>
<html lang="en">
<head>
<meta charset="utf-8">
<title>Homestead Capital Partners – Business Card</title>
<link rel="stylesheet" href="https://fonts.googleapis.com/css2?family=Saira+Condensed:wght@500;600;700&family=Arimo:wght@400&display=swap">
<style>
  :root {
    --page: #eeeeec;
    --burgundy-core: #7a1a2e;
    --burgundy-mid: #5e1222;
    --burgundy-edge: #330812;
    --platinum: #e4e4e4;
    --platinum-dark: #b9b9b9;
    --ink-light: #f1dde2;
    --ink-soft: #e9d6db;
    --name-ink: #6e1528;
  }
  * { box-sizing: border-box; margin: 0; padding: 0; }
  html, body { width: 825px; height: 1200px; overflow: hidden; }
  body {
    background: var(--page);
    display: flex;
    flex-direction: column;
    align-items: center;
    justify-content: center;
    gap: 110px;
  }
  .card {
    position: relative;
    width: 520px;
    height: 300px;
    overflow: hidden;
    background: radial-gradient(ellipse at 45% 35%, var(--burgundy-core) 0%, var(--burgundy-mid) 55%, var(--burgundy-edge) 100%);
    box-shadow: 0 6px 18px rgba(0,0,0,.25);
  }
  .tagline {
    position: absolute;
    left: 46px;
    top: 46px;
    font-family: "Saira Condensed", sans-serif;
    font-weight: 600;
    font-size: 17px;
    letter-spacing: .5px;
    line-height: 24px;
    color: var(--ink-light);
    text-transform: uppercase;
  }
  .name-band {
    position: absolute;
    left: 0;
    top: 128px;
    width: 520px;
    height: 50px;
    background: linear-gradient(180deg, #f2f2f2 0%, var(--platinum) 60%, var(--platinum-dark) 100%);
    box-shadow: 0 2px 5px rgba(0,0,0,.35);
  }
  .agent-name {
    position: absolute;
    left: 44px;
    top: 5px;
    font-family: "Saira Condensed", sans-serif;
    font-weight: 700;
    font-size: 24px;
    line-height: 26px;
    color: var(--name-ink);
    letter-spacing: .5px;
  }
  .agent-title {
    position: absolute;
    left: 44px;
    top: 31px;
    font-family: "Saira Condensed", sans-serif;
    font-weight: 600;
    font-size: 11px;
    color: var(--name-ink);
    letter-spacing: .4px;
  }
  .renovation-photo {
    position: absolute;
    left: 270px;
    top: 108px;
    width: 200px;
    height: 74px;
    background: linear-gradient(90deg, #9a6a3c 0%, #b58753 40%, #8d9198 55%, #6f747c 100%);
  }
  .before-after {
    position: absolute;
    left: 290px;
    top: 186px;
    display: flex;
    align-items: center;
    gap: 4px;
    font-family: "Saira Condensed", sans-serif;
    font-weight: 600;
    font-size: 11px;
    color: var(--ink-light);
    letter-spacing: .5px;
  }
  .contact-list {
    position: absolute;
    left: 50px;
    top: 222px;
    list-style: none;
    font-family: "Arimo", sans-serif;
    font-size: 15px;
    line-height: 22px;
    color: var(--ink-soft);
  }
  .contact-list li { display: flex; align-items: center; gap: 8px; }
  .company-block {
    position: absolute;
    left: 0;
    top: 138px;
    width: 520px;
    text-align: center;
  }
  .company-name {
    display: inline-flex;
    align-items: center;
    gap: 10px;
    font-family: "Saira Condensed", sans-serif;
    font-weight: 700;
    font-size: 24px;
    color: var(--platinum);
    letter-spacing: .6px;
  }
  .company-name .mark {
    width: 14px;
    height: 14px;
    background: var(--platinum);
  }
  .address {
    margin-top: 4px;
    display: inline-flex;
    align-items: center;
    gap: 6px;
    font-family: "Arimo", sans-serif;
    font-size: 14px;
    color: var(--platinum);
    letter-spacing: .3px;
  }
</style>
</head>
<body>
  <section class="card card-front">
    <p class="tagline">I buy Marsh Hollow homes for cash, quick closings...<br>Renewing Marsh Hollow, one home at a time...</p>
    <div class="name-band">
      <h1 class="agent-name">RAY T. BELLAMY CIAS</h1>
      <p class="agent-title">REALTOR/CERTIFIED INVESTOR AGENT</p>
    </div>
    <div class="renovation-photo" role="img" aria-label="Photo of a house before renovation beside the same house after renovation"></div>
    <div class="before-after">
      <span>BEFORE</span>
      <svg width="64" height="8" viewBox="0 0 64 8" aria-hidden="true">
        <circle cx="3" cy="4" r="2" fill="#f1dde2"/>
        <line x1="6" y1="4" x2="58" y2="4" stroke="#f1dde2" stroke-width="1" stroke-dasharray="2 2"/>
        <path d="M57 1 L62 4 L57 7 Z" fill="#f1dde2"/>
      </svg>
      <span>AFTER</span>
    </div>
    <ul class="contact-list">
      <li>
        <svg width="12" height="12" viewBox="0 0 24 24" aria-hidden="true"><path fill="#e9d6db" d="M6.6 10.8a15.1 15.1 0 0 0 6.6 6.6l2.2-2.2c.3-.3.7-.4 1-.2 1.1.4 2.3.6 3.6.6.6 0 1 .4 1 1V20c0 .6-.4 1-1 1A17 17 0 0 1 3 4c0-.6.4-1 1-1h3.5c.6 0 1 .4 1 1 0 1.3.2 2.5.6 3.6.1.3 0 .7-.2 1z"/></svg>
        843.555.0172
      </li>
      <li>
        <svg width="12" height="10" viewBox="0 0 24 18" aria-hidden="true"><rect x="1" y="1" width="22" height="16" rx="1" fill="#e9d6db"/><path d="M1 1 L12 10 L23 1" fill="none" stroke="#5e1222" stroke-width="2"/></svg>
        raybellamyhouses@quillmail.example
      </li>
    </ul>
  </section>

  <section class="card card-back">
    <div class="company-block">
      <h2 class="company-name"><span class="mark"></span>HOMESTEAD CAPITAL PARTNERS, LLC.</h2>
      <br>
      <p class="address">
        <svg width="10" height="13" viewBox="0 0 20 26" aria-hidden="true"><path fill="#e4e4e4" d="M10 0a10 10 0 0 0-10 10c0 7 10 16 10 16s10-9 10-16A10 10 0 0 0 10 0zm0 14a4 4 0 1 1 0-8 4 4 0 0 1 0 8z"/></svg>
        P.O. BOX 86, MARSH HOLLOW, S.C. 29401
      </p>
    </div>
  </section>
</body>
</html>
```